Attract renters to our neighborhoods - inform renters who we are

Apartments in several neighborhoods. We want to attract renters who want to live along the lake or other near by neighborhoods. We want them to know that we have an apartment for them in their location.
The perfect location to spend your time.
When minutes matter LIVE where you work and play! (love this tag line)
Updates

www.kvtresidences.example Choose from over 3,700 apartments in Chicago’s most celebrated neighborhoods. 773-582-6041 Chicago’s most celebrated neighborhoods. 31 PROPERTIES

Target Market(s)

Sophisticated apartment renter who wants location, space, amenities

Industry/Entity Type

Apartment Rentals

Requirements
Must have
• Feel like I want to live there, or the ad is calling me
Nice to have
• Appeal to a sophisticated apartment renter. We have what you want, where you want to be.
Should not have
• Logo colors are black and red/burnt orange see attached logo

```html
<!DOCTYPE html>
<html lang="en">
<head>
<meta charset="utf-8">
<title>KVT Apartments Flyer</title>
<link href="https://fonts.googleapis.com/css2?family=Poppins:wght@400;600;700&display=swap" rel="stylesheet">
<style>
  :root {
    --ink: #111111;
    --brand-red: #b11f2e;
    --band: rgba(58, 58, 64, 0.92);
    --deco-grey: #c2c2c2;
    --paper: #ffffff;
    --stage: #d6d6d6;
    --white: #ffffff;
  }
  * { margin: 0; padding: 0; box-sizing: border-box; }
  html, body {
    width: 1031px; height: 1200px; overflow: hidden;
    background: var(--stage);
    font-family: "Poppins", sans-serif;
  }
  .flyer {
    position: absolute; left: 51px; top: 0;
    width: 928px; height: 1200px;
    background: var(--paper);
    overflow: hidden;
  }
  .hero-photo {
    position: absolute; left: 0; top: 0;
    width: 791px; height: 893px;
    clip-path: polygon(0 0, 791px 0, 791px 216px, 301px 893px, 0 893px);
    background: linear-gradient(160deg, #d9d1c6 0%, #c9b8a2 35%, #b9a48c 60%, #8f7a6a 100%);
  }
  .headline-band {
    position: absolute; left: 0; top: 63px;
    width: 791px; height: 271px;
    background: var(--band);
  }
  .headline {
    position: absolute; left: 72px; top: 78px;
    color: var(--white);
    font-weight: 400; font-size: 52px; line-height: 64.5px;
    letter-spacing: -0.5px;
  }
  .headline strong { font-weight: 700; }
  .corner-deco { position: absolute; left: 791px; top: 0; }
  .offer {
    position: absolute; left: 520px; top: 632px; width: 390px;
    color: var(--ink);
  }
  .offer-title { font-weight: 700; font-size: 21.5px; line-height: 30px; }
  .locations { list-style: none; margin-top: 18px; }
  .locations li {
    display: flex; align-items: center; gap: 10px;
    font-size: 21px; line-height: 36.5px;
  }
  .locations svg { width: 18px; height: 18px; flex: none; }
  .tagline {
    margin-top: 18px;
    color: var(--brand-red); font-weight: 700;
    font-size: 28px; line-height: 35px;
  }
  .contact { position: absolute; left: 54px; top: 1000px; color: var(--ink); }
  .contact-call {
    color: var(--brand-red); font-weight: 700;
    font-size: 36px; line-height: 44px;
  }
  .contact-body {
    margin-top: 8px; font-size: 24px; line-height: 31px;
  }
  .contact-body strong { font-weight: 700; }
  .brand-name {
    position: absolute; left: 525px; top: 1040px;
    display: flex; align-items: center; gap: 14px;
  }
  .brand-name span {
    color: var(--ink); font-weight: 700; font-size: 96px; line-height: 1;
    letter-spacing: -2px;
  }
  .brand-name i {
    display: block; width: 22px; height: 22px; background: var(--brand-red);
  }
  .footer-bar {
    position: absolute; left: 0; bottom: 0;
    width: 928px; height: 17px; background: var(--ink);
  }
</style>
</head>
<body>
  <main class="flyer">
    <div class="hero-photo" role="img" aria-label="Bright modern apartment living room with beige sofa, round glass coffee table, patterned rug, open kitchen and floating wooden staircase"></div>

    <div class="headline-band"></div>
    <h1 class="headline">WHEN <strong>MINUTES</strong><br><strong>MATTER</strong> LIVE<br>WHERE YOU WORK<br>AND PLAY!</h1>

    <svg class="corner-deco" width="137" height="216" viewBox="0 0 137 216" aria-hidden="true">
      <rect x="0" y="0" width="50" height="216" fill="var(--deco-grey)"/>
      <polygon points="50,0 137,0 137,210 50,88" fill="var(--deco-grey)"/>
      <polygon points="72,0 84,0 137,72 137,90" fill="var(--paper)"/>
      <polygon points="100,24 137,24 137,36 108,36" fill="var(--paper)"/>
      <polygon points="120,58 137,58 137,66 125,66" fill="var(--paper)"/>
    </svg>

    <section class="offer">
      <h2 class="offer-title">Pristine Apartments Available<br>in celebrated Locations.</h2>
      <ul class="locations">
        <li><svg viewBox="0 0 18 18"><path d="M9 2a4.5 4.5 0 0 0-4.5 4.5C4.5 10 9 14 9 14s4.5-4 4.5-7.5A4.5 4.5 0 0 0 9 2z" fill="none" stroke="var(--brand-red)" stroke-width="1.3"/><circle cx="9" cy="6.5" r="1.6" fill="none" stroke="var(--brand-red)" stroke-width="1.3"/><path d="M2 16.5h14l-2-3H4z" fill="none" stroke="var(--brand-red)" stroke-width="1.1"/></svg>Gold Coast &amp; Old Town</li>
        <li><svg viewBox="0 0 18 18"><path d="M9 2a4.5 4.5 0 0 0-4.5 4.5C4.5 10 9 14 9 14s4.5-4 4.5-7.5A4.5 4.5 0 0 0 9 2z" fill="none" stroke="var(--brand-red)" stroke-width="1.3"/><circle cx="9" cy="6.5" r="1.6" fill="none" stroke="var(--brand-red)" stroke-width="1.3"/><path d="M2 16.5h14l-2-3H4z" fill="none" stroke="var(--brand-red)" stroke-width="1.1"/></svg>River North</li>
        <li><svg viewBox="0 0 18 18"><path d="M9 2a4.5 4.5 0 0 0-4.5 4.5C4.5 10 9 14 9 14s4.5-4 4.5-7.5A4.5 4.5 0 0 0 9 2z" fill="none" stroke="var(--brand-red)" stroke-width="1.3"/><circle cx="9" cy="6.5" r="1.6" fill="none" stroke="var(--brand-red)" stroke-width="1.3"/><path d="M2 16.5h14l-2-3H4z" fill="none" stroke="var(--brand-red)" stroke-width="1.1"/></svg>Lincoln Park</li>
        <li><svg viewBox="0 0 18 18"><path d="M9 2a4.5 4.5 0 0 0-4.5 4.5C4.5 10 9 14 9 14s4.5-4 4.5-7.5A4.5 4.5 0 0 0 9 2z" fill="none" stroke="var(--brand-red)" stroke-width="1.3"/><circle cx="9" cy="6.5" r="1.6" fill="none" stroke="var(--brand-red)" stroke-width="1.3"/><path d="M2 16.5h14l-2-3H4z" fill="none" stroke="var(--brand-red)" stroke-width="1.1"/></svg>Lakeview</li>
      </ul>
      <p class="tagline">The perfect location<br>to spend your time.</p>
    </section>

    <section class="contact">
      <p class="contact-call">CALL +000 000 000</p>
      <p class="contact-body">Choose from over <strong>3,700</strong><br>apartments in chicago’s most<br>celbrated neighbourhoods</p>
    </section>

    <div class="brand-name"><span>KVT</span><i></i></div>

    <div class="footer-bar"></div>
  </main>
</body>
</html>
```